Brass Kite Gig - 20 Years of Funk

I'm with a funk band called Brass Kite. We are celebrating our 20 year anniversary with a show on August 3, 2024. We would like some banners made for social media to help promote the gig. I'm attaching some examples of our 10 year anniversary gig so you can at least get an idea of what we are looking for.

Here's the text for the banners:
BRASS KITE Anniversary Gig - 20 Years of Funk!
Saturday, August 10, 2024
with special guest: Marco Delvin
Doors at 7pm, Show at 8pm

We would like three sizes:
1920 x 1005 pixels
1080 x 1080 pixels
1080 x 1920 pixels

You can check out our website for more ideas of our graphic style, etc.. www.brasskiteband.example

```html
<!DOCTYPE html>
<html lang="en">
<head>
<meta charset="utf-8">
<title>Brass Kite Anniversary Gig – 20 Years of Funk</title>
<link rel="stylesheet" href="https://fonts.googleapis.com/css2?family=Titan+One&family=Oswald:wght@500;600&family=Josefin+Sans:wght@300;400;700&display=swap">
<style>
  :root {
    --lime: #c5dc2a;
    --lime-deep: #6f7d14;
    --ink: #050505;
    --paper: #ffffff;
    --white: #ffffff;
  }
  html, body {
    margin: 0;
    padding: 0;
    width: 1200px;
    height: 1200px;
    overflow: hidden;
    background: var(--paper);
  }
  .canvas {
    position: relative;
    width: 1200px;
    height: 1200px;
    background: var(--paper);
  }
  .banner {
    position: absolute;
    left: 0;
    top: 287px;
    width: 1200px;
    height: 627px;
    overflow: hidden;
    background: var(--ink);
  }
  .stage-photo {
    position: absolute;
    inset: 0;
    background:
      radial-gradient(ellipse 520px 420px at 230px 200px, rgba(197,220,42,0.55), rgba(197,220,42,0) 70%),
      radial-gradient(ellipse 360px 300px at 520px 470px, rgba(160,180,30,0.45), rgba(0,0,0,0) 70%),
      linear-gradient(90deg, #4b5510 0%, #2b310a 35%, #0d0f03 62%, #050505 100%);
  }
  .wordmark {
    position: absolute;
    left: 308px;
    top: 56px;
    margin: 0;
    font-family: "Josefin Sans", sans-serif;
    font-weight: 700;
    font-size: 84px;
    line-height: 1;
    color: var(--lime);
    white-space: nowrap;
  }
  .subtitle {
    position: absolute;
    left: 300px;
    top: 166px;
    margin: 0;
    font-family: "Josefin Sans", sans-serif;
    font-weight: 400;
    font-size: 33px;
    letter-spacing: 0.13em;
    color: var(--white);
    white-space: nowrap;
  }
  .headline {
    position: absolute;
    right: 30px;
    top: 44px;
    margin: 0;
    text-align: right;
    font-family: "Titan One", sans-serif;
    font-weight: 400;
    font-size: 74px;
    line-height: 0.92;
    color: var(--white);
    text-shadow: 4px 5px 0 var(--ink), 6px 7px 0 var(--lime);
  }
  .date {
    position: absolute;
    right: 37px;
    top: 232px;
    margin: 0;
    text-align: right;
    font-family: "Oswald", sans-serif;
    font-weight: 600;
    font-size: 46px;
    line-height: 1.02;
    color: var(--white);
    letter-spacing: 0.02em;
  }
  .date .accent { color: var(--lime); margin-left: 6px; }
  .guest-label {
    position: absolute;
    left: 667px;
    top: 322px;
    margin: 0;
    font-family: "Josefin Sans", sans-serif;
    font-weight: 400;
    font-size: 26px;
    letter-spacing: 0.42em;
    color: var(--white);
  }
  .guest-name {
    position: absolute;
    right: 37px;
    top: 358px;
    margin: 0;
    font-family: "Josefin Sans", sans-serif;
    font-weight: 300;
    font-size: 54px;
    letter-spacing: 0.04em;
    color: var(--lime);
    white-space: nowrap;
  }
  .times {
    position: absolute;
    right: 32px;
    top: 430px;
    margin: 0;
    text-align: right;
    font-family: "Titan One", sans-serif;
    font-size: 64px;
    line-height: 1.2;
    color: var(--white);
    text-shadow: 3px 4px 0 var(--ink), 5px 6px 0 var(--lime);
  }
  .times .accent { color: var(--lime); text-shadow: 3px 4px 0 var(--ink), 5px 6px 0 var(--white); }
  .badge {
    position: absolute;
    left: 151px;
    top: 399px;
    width: 314px;
    height: 314px;
  }
  .badge-name {
    position: absolute;
    left: 151px;
    top: 534px;
    width: 314px;
    margin: 0;
    text-align: center;
    font-family: "Josefin Sans", sans-serif;
    font-weight: 700;
    font-size: 44px;
    color: var(--lime);
  }
</style>
</head>
<body>
  <main class="canvas">
    <section class="banner">
      <div class="stage-photo" role="img" aria-label="Lime-tinted live photo of the band's singer pointing at the crowd with a trombone player behind him"></div>

      <h1 class="wordmark">Brass Kite</h1>
      <p class="subtitle">ANNIVERSARY GIG</p>

      <h2 class="headline">20 YEARS<br>OF FUNK!</h2>

      <p class="date">SATURDAY<span class="accent">AUGUST 10</span><br>2024</p>

      <p class="guest-label">SPECIAL GUEST</p>
      <p class="guest-name">MARCO DELVIN</p>

      <p class="times">DOORS <span class="accent">AT 7PM</span><br><span class="accent">SHOW</span> AT 8PM</p>

      <svg class="badge" viewBox="0 0 314 314" aria-hidden="true">
        <circle cx="157" cy="157" r="146" fill="var(--ink)" stroke="var(--lime)" stroke-width="20"/>
      </svg>
      <p class="badge-name">Brass Kite</p>
    </section>
  </main>
</body>
</html>
```